Restaurant Finder Website Design

I need to create a website that will help people find restaurants around a zip code or address.

I would like to have a very clean and simple design. I will need a design for the homepage, that should be very clean and simple to use. its where the users will launch their search. I am thinking something like pomira like.. big search field with a very clean page where users can create an account or restaurants subscribe to the service.

Also need the design of the search results page, I would like to display a big map with the results and a list on the side or the bottom of the map.

Also need a profile page for the users that sign up to the site.

Mostly what I need are guidelines and color coordinated elements, like a general layout and buttons that work together. I would like to know what the action buttons and elements should look like. Because its going to have some more detail pages.

Target Market(s)

People in general, mainly people that work at an office and have to find a place for lunch every day.

Industry/Entity Type

Restaurant

Number of Pages Required

4 page

Font styles to use
Serif
Sans Serif

Requirements
Must have
• It must be a really simple and clean design but look edgy.

```html
<!DOCTYPE html>
<html lang="en">
<head>
<meta charset="utf-8">
<title>Forkwise – Find a place to eat</title>
<link rel="stylesheet" href="https://fonts.googleapis.com/css2?family=Raleway:wght@300;400;600;700&family=Lato:wght@400;700&display=swap">
<style>
  :root {
    --brand-red: #cc0000;
    --ink-navy: #1f2a38;
    --ink-dark: #333333;
    --paper: #ffffff;
    --header-bg: #f4f4f4;
    --footer-black: #000000;
    --muted: #9a9a9a;
  }
  * { box-sizing: border-box; margin: 0; padding: 0; }
  html, body { width: 1200px; height: 570px; overflow: hidden; }
  body { position: relative; font-family: "Raleway", sans-serif; background: var(--paper); }

  .site-header {
    position: absolute; left: 0; top: 0; width: 1200px; height: 76px;
    background: linear-gradient(#ffffff, #ececec);
    border-bottom: 2px solid var(--brand-red);
  }
  .brand { position: absolute; display: flex; align-items: center; gap: 8px; }
  .brand-mark { width: 50px; height: 50px; border-radius: 50%; background: var(--brand-red); }
  .brand-name { font-family: "Raleway", sans-serif; font-weight: 600; font-size: 27px; }
  .site-header .brand { left: 161px; top: 12px; }
  .site-header .brand-name { color: var(--ink-dark); }

  .btn {
    position: absolute; display: flex; align-items: center; justify-content: center;
    font-family: "Raleway", sans-serif; font-weight: 700; font-size: 12px;
    color: var(--paper); text-transform: uppercase; text-decoration: none;
  }
  .btn-login { left: 854px; top: 21px; width: 80px; height: 31px; background: var(--ink-navy); }
  .btn-register { left: 942px; top: 21px; width: 97px; height: 31px; background: var(--brand-red); }

  .hero { position: absolute; left: 0; top: 76px; width: 1200px; height: 384px; }
  .hero-photo {
    position: absolute; inset: 0;
    background:
      radial-gradient(ellipse 300px 180px at 850px 180px, #2b2a3e 0%, transparent 70%),
      radial-gradient(ellipse 260px 120px at 600px 40px, #c9a84a 0%, transparent 75%),
      radial-gradient(ellipse 520px 260px at 300px 260px, #d8c3a0 0%, transparent 75%),
      linear-gradient(120deg, #8a5a36, #b9926b 45%, #6e4a33);
  }
  .hero-shade { position: absolute; inset: 0; background: rgba(0,0,0,0.22); }
  .hero-title {
    position: absolute; left: 0; width: 1200px; top: 146px; text-align: center;
    color: var(--paper); font-weight: 700; font-size: 32px; top: 70px;
  }
  .search-panel {
    position: absolute; left: 326px; top: 123px; width: 537px; height: 62px;
    background: rgba(40,40,40,0.75);
  }
  .search-input {
    position: absolute; left: 12px; top: 12px; width: 440px; height: 40px;
    background: var(--paper); border: 0; padding-left: 17px;
    font-family: "Raleway", sans-serif; font-size: 13px; color: var(--muted);
    display: flex; align-items: center;
  }
  .search-button {
    position: absolute; left: 450px; top: 12px; width: 75px; height: 40px;
    background: var(--brand-red); color: var(--paper); font-weight: 700; font-size: 13px;
    display: flex; align-items: center; justify-content: center;
  }
  .search-button::before {
    content: ""; position: absolute; left: -6px; top: 14px;
    border-top: 6px solid transparent; border-bottom: 6px solid transparent;
    border-right: 6px solid var(--brand-red);
  }
  .owner-title {
    position: absolute; left: 0; width: 1200px; top: 201px; text-align: center;
    color: var(--paper); font-weight: 700; font-size: 31px;
  }
  .owner-sub {
    position: absolute; left: 0; width: 1200px; top: 241px; text-align: center;
    color: #eeeeee; font-weight: 300; font-size: 18px;
  }
  .btn-owner { left: 552px; top: 274px; width: 96px; height: 32px; background: var(--brand-red); font-family: "Lato", sans-serif; font-size: 12px; }

  .site-footer { position: absolute; left: 0; top: 460px; width: 1200px; height: 74px; background: var(--brand-red); }
  .footer-nav { position: absolute; left: 163px; top: 12px; display: flex; gap: 8px; font-family: "Lato", sans-serif; font-weight: 700; font-size: 12px; color: var(--paper); }
  .follow { position: absolute; left: 163px; top: 40px; display: flex; align-items: center; gap: 6px; color: var(--paper); font-family: "Lato", sans-serif; font-size: 14px; }
  .follow-label { margin-right: 4px; }
  .social-dot { width: 21px; height: 21px; border-radius: 50%; background: var(--paper); }
  .site-footer .brand { left: 837px; top: 8px; }
  .site-footer .brand-mark { background: var(--paper); width: 50px; height: 50px; }
  .site-footer .brand-name { color: var(--paper); font-size: 27px; }

  .legal-bar { position: absolute; left: 0; top: 534px; width: 1200px; height: 36px; background: var(--footer-black); color: #dddddd; font-family: "Lato", sans-serif; font-size: 11.5px; }
  .copyright { position: absolute; left: 162px; top: 11px; }
  .legal-links { position: absolute; right: 161px; top: 11px; display: flex; gap: 14px; }
  .legal-links .sep { color: #444444; }
</style>
</head>
<body>
  <header class="site-header">
    <div class="brand"><span class="brand-mark"></span><span class="brand-name">Forkwise</span></div>
    <a class="btn btn-login" href="#">Login</a>
    <a class="btn btn-register" href="#">Register</a>
  </header>

  <section class="hero">
    <div class="hero-photo" role="img" aria-label="Close-up photo of a plate of quesadillas with rice, black beans and fresh salsa"></div>
    <div class="hero-shade"></div>
    <h1 class="hero-title">WHAT WOULD YOU LIKE TO EAT TODAY?</h1>
    <div class="search-panel">
      <div class="search-input">Zip Code or Address</div>
      <div class="search-button">SEARCH</div>
    </div>
    <h2 class="owner-title">Are you a restaurant?</h2>
    <p class="owner-sub">Create your account here</p>
    <a class="btn btn-owner" href="#">Register</a>
  </section>

  <footer class="site-footer">
    <nav class="footer-nav">
      <span>Home</span><span>|</span><span>What's This?</span><span>|</span><span>Dish</span><span>|</span><span>Places</span><span>|</span><span>Blog</span><span>|</span><span>Contact Us</span>
    </nav>
    <div class="follow"><span class="follow-label">Follow Us :</span><span class="social-dot"></span><span class="social-dot"></span><span class="social-dot"></span></div>
    <div class="brand"><span class="brand-mark"></span><span class="brand-name">Forkwise</span></div>
  </footer>

  <div class="legal-bar">
    <p class="copyright">© Copyright 2016 &nbsp;Forkwise. &nbsp;| All Rights Reserved</p>
    <div class="legal-links"><span>Terms Of Use</span><span class="sep">|</span><span>Privacy Statements</span></div>
  </div>
</body>
</html>
```